Coach company requires modern brochure

We need a brochure designed that shows our various coach services. The aim of the brochure is to attract new business, therefore we need something that is modern, eye-catching and uses a lot of imagery/design rather than being text heavy.

I have all the images that can be sent via dropbox or google drive if you want to request them.

Target Market(s)

Wedding planners, event companies, school business managers, sporting groups

Industry/Entity Type

Tourism

Requirements
Must have
• 4 x a4 pages
• Bold and eye catching cover page

```html
<!DOCTYPE html>
<html lang="en">
<head>
<meta charset="utf-8">
<title>Ridgeway Coast Coaches – Services Brochure</title>
<link rel="stylesheet" href="https://fonts.googleapis.com/css2?family=Open+Sans:wght@400;600&family=Lora:ital,wght@1,400;1,700&display=swap">
<style>
  :root {
    --backdrop: #2b2b2b;
    --paper: #f4f6f8;
    --paper-shade: #e6eaee;
    --green: #8cc63f;
    --green-dark: #3d8b2f;
    --blue: #6aa9e6;
    --text: #4a4a4a;
    --photo-frame: #ffffff;
  }
  * { box-sizing: border-box; margin: 0; padding: 0; }
  html, body { width: 1200px; height: 789px; overflow: hidden; background: var(--backdrop); }
  body { font-family: "Open Sans", Arial, sans-serif; color: var(--text); position: relative; }

  .spread { position: absolute; left: 105px; top: 44px; width: 990px; height: 700px; display: flex; box-shadow: 0 10px 40px rgba(0,0,0,.5); }
  .page { position: relative; width: 495px; height: 700px; background: linear-gradient(180deg, var(--paper) 0%, #ffffff 55%, var(--paper-shade) 100%); overflow: hidden; }
  .page--left { box-shadow: inset -18px 0 24px -18px rgba(0,0,0,.25); }
  .page--right { box-shadow: inset 18px 0 24px -18px rgba(0,0,0,.25); }

  .section-tab { position: absolute; height: 20px; width: 195px; background: var(--green); color: #fff;
    font-family: "Lora", Georgia, serif; font-style: italic; font-weight: 400; font-size: 12.5px; line-height: 20px; padding-left: 14px; }
  .section-tab::after { content: ""; position: absolute; right: -8px; top: 0; width: 6px; height: 20px; background: var(--blue); transform: skewX(-18deg); }

  .body-copy { position: absolute; font-size: 7.8px; line-height: 1.42; text-align: justify; }

  .photo { position: absolute; border: 4px solid var(--photo-frame); box-shadow: 0 3px 8px rgba(0,0,0,.35); }
  .photo--driver { background: linear-gradient(135deg, #3f6d3a, #8ea7c0 60%, #dfe6ee); }
  .photo--reception { background: linear-gradient(135deg, #f0f2f2, #cfd6d8 60%, #7fc6c0); }
  .photo--road { background: linear-gradient(180deg, #b9c7c9, #5e7a55 50%, #3a3f3c); }
  .photo--group { background: linear-gradient(180deg, #9fb8c9, #4d6c4a 45%, #6a9ac9 70%, #8a8a84); }
  .photo--lookout { background: linear-gradient(180deg, #dfe9ee, #6e8f5a 50%, #4b3a2a); }

  .testimonial { position: absolute; font-family: "Lora", Georgia, serif; font-style: italic; font-weight: 700;
    color: var(--green-dark); font-size: 9px; line-height: 1.4; text-align: justify; }
  .quote-mark { position: absolute; font-family: "Lora", Georgia, serif; font-weight: 700; font-size: 44px; color: #a9a9a9; line-height: 1; }

  .page-wave { position: absolute; left: 0; bottom: 0; width: 495px; }

  .circle-photo { position: absolute; border-radius: 50%; border: 4px solid #fff; box-shadow: 0 2px 6px rgba(0,0,0,.3); }
  .circle-photo--crowd { background: linear-gradient(180deg, #cfd9c5, #8f9b7c 60%, #6d6a5e); }
  .circle-photo--palm { background: linear-gradient(180deg, #2f66b8, #6fa3d8 55%, #e7ecef); }
  .circle-photo--stadium { background: linear-gradient(180deg, #6b4e4e, #b98f8f 35%, #3fa14b 60%, #2e8a3c); }

  .web-address { position: absolute; left: 150px; bottom: 26px; font-family: "Lora", Georgia, serif; font-size: 15px; color: #2f3a2a; display: flex; align-items: center; gap: 8px; }
  .web-address .globe { width: 12px; height: 12px; border: 1.5px solid #2f3a2a; border-radius: 50%; }
</style>
</head>
<body>
<main class="spread">

  <section class="page page--left">
    <svg class="page-wave" style="height:150px;" viewBox="0 0 495 150" preserveAspectRatio="none" aria-hidden="true">
      <path d="M0 50 C 140 100, 330 140, 495 115 L495 150 L0 150 Z" fill="var(--blue)"/>
      <path d="M0 60 C 140 112, 330 150, 495 126 L495 150 L0 150 Z" fill="var(--green)"/>
    </svg>

    <h2 class="section-tab" style="left:40px; top:28px;">About Us</h2>
    <p class="body-copy" style="left:40px; top:58px; width:262px;">
      Ridgeway Coast Coaches is the first choice of wedding, corporate and conference event planners from Caloundra to Gympie and everywhere in between. With a reputation for a reliable, punctual and courteous service, we hand pick our experienced drivers from the Sunshine Coast region to ensure they maintain the high standards for which we are known. Our fleet of modern, comfortable and well maintained buses are fitted with seat belts and air-conditioning, and some include TV/DVD facilities. Ranging in size from 13 to 57 seat buses, we can deliver on a wide variety of bus charter needs, from small groups often through to corporate events requiring the transport of 300 passengers, anywhere on the Sunshine Coast.
    </p>
    <div class="photo photo--driver" role="img" aria-label="Driver standing beside a white coach" style="left:312px; top:70px; width:145px; height:105px;"></div>

    <h2 class="section-tab" style="left:40px; top:218px;">Weddings &amp; Events</h2>
    <div class="photo photo--reception" role="img" aria-label="Wedding reception table setting" style="left:40px; top:248px; width:155px; height:102px;"></div>
    <p class="body-copy" style="left:207px; top:252px; width:250px;">
      With its pristine beaches, spectacular mountains and fantastic venues, the Sunshine Coast is fast becoming one of the most popular locations for weddings. Whether you are saying "I do" under a flowering jacaranda in the hinterland, we can transport you and your guests on your special day. Choosing one of our vehicles to transfer guests to and from your reception is the best way to move your family and friends easily while ensuring everything runs to schedule. Why not consider hiring one of our buses to transport your bridal party to different venues on the coast? There's plenty of space for everyone, including the wedding dress!
    </p>

    <h2 class="section-tab" style="left:40px; top:388px;">Events</h2>
    <p class="body-copy" style="left:40px; top:418px; width:258px;">
      Attending a long lunch on a private estate, or hosting a special birthday at one of the Sunshine Coast's amazing dining venues? If you can't decide on who should be the designated driver then fear not, we can take the pressure of this decision for you. Our extensive range of fully air-conditioned coaches can fit groups from 4 to 200 so get in touch today and allow us to add the finishing touch to your special event.
    </p>
    <div class="photo photo--road" role="img" aria-label="Country road lined with trees" style="left:312px; top:410px; width:145px; height:102px;"></div>

    <span class="quote-mark" style="left:58px; top:505px;">&ldquo;</span>
    <blockquote class="testimonial" style="left:90px; top:522px; width:300px;">
      It was an incredible day and I honestly cannot thank Mark enough for his time and assistance with the co-ordination of the delivery of service and buses on the day. Everything ran seamlessly which enhanced our clients overall experience. The feedback received to date has been fabulous' Laura, Open Road Events.
    </blockquote>
    <span class="quote-mark" style="left:398px; top:580px;">&rdquo;</span>
  </section>

  <section class="page page--right">
    <svg class="page-wave" style="height:200px;" viewBox="0 0 495 200" preserveAspectRatio="none" aria-hidden="true">
      <path d="M0 50 C 160 95, 340 100, 495 55 L495 200 L0 200 Z" fill="var(--blue)"/>
      <path d="M0 63 C 160 110, 340 115, 495 72 L495 200 L0 200 Z" fill="var(--green)"/>
    </svg>

    <h2 class="section-tab" style="left:40px; top:28px;">Corporate Groups</h2>
    <p class="body-copy" style="left:40px; top:58px; width:255px;">
      Ridgeway Coast Coaches can take some of the pressure off organising your next corporate event. With an extensive range of vehicles in our fleet, we can offer a reliable, punctual and professional service for all group sizes. We pride ourselves on our knowledge of corporate venues, and are the go to partner for a number of Event Planners across the Sunshine Coast.
    </p>
    <div class="photo photo--group" role="img" aria-label="Group of staff in blue shirts beside golf carts" style="left:312px; top:95px; width:145px; height:102px;"></div>
    <span class="quote-mark" style="left:36px; top:132px;">&ldquo;</span>
    <blockquote class="testimonial" style="left:40px; top:160px; width:258px;">
      This service has proven invaluable, and as this is a Community Event, we are sincerely grateful for the invaluable shuttle transport service provided to our Festival (which is a not for profit organisation) by Ridgeway Coast Coaches. It is due to their support, we continue to maintain a very cost effective 'Community' driven ticket price for families to attend this great event.' Tom Ferris, Festival Director, Bayside Long Weekend Festival
    </blockquote>

    <h2 class="section-tab" style="left:40px; top:282px;">Educational Groups</h2>
    <div class="photo photo--lookout" role="img" aria-label="Coastal lookout with palm trees" style="left:40px; top:312px; width:155px; height:102px;"></div>
    <p class="body-copy" style="left:207px; top:330px; width:250px;">
      In addition to our regular school bus runs, we are also able to provide transport options for a wide range of other educational excursions. Be it day trips, school camps or sporting events, we can provide services for primary and secondary schools, as well as colleges and language schools. In addition to local schools, we can also provide Brisbane schools with a safe, reliable and great value transport option for camps on the Sunshine Coast.
    </p>
    <span class="quote-mark" style="left:425px; top:295px;">&rdquo;</span>

    <h2 class="section-tab" style="left:40px; top:428px;">Sporting Groups</h2>
    <p class="body-copy" style="left:40px; top:458px; width:250px;">
      Getting away with your team for a match or game and need some transport? We have an extensive fleet as well as spacious luggage trailers for your equipment, so let us know your dates and group size and we can easily organise your quote and booking.
    </p>

    <div class="circle-photo circle-photo--crowd" role="img" aria-label="Visitors on a day outing" style="left:215px; top:512px; width:70px; height:70px;"></div>
    <div class="circle-photo circle-photo--palm" role="img" aria-label="Palm tree against blue sky" style="left:290px; top:500px; width:84px; height:84px;"></div>
    <div class="circle-photo circle-photo--stadium" role="img" aria-label="Football stadium pitch" style="left:380px; top:480px; width:106px; height:106px;"></div>

    <p class="web-address"><span class="globe"></span>www.ridgeway-coast-coaches.com</p>
  </section>

</main>
</body>
</html>
```